GDFH Business Card

Looking for a business card design to incorporate our branding. We want to only use the colors listing in the Branding Package (attached).
Updates

Target Market(s)

People who need their phone or device fixed.

Industry/Entity Type

Electronics

Contact Information for Business Card

Please use:

Gadget Fix Haven LLC
4870 S Ridgecrest Pkwy
Suite 318
San Antonio, TX 78291

Wendell Thorsby, Store Manager

(210) 555-0147

Requirements
Must have
• Must include the colors that are contained within the Branding Package PDF file.

```html
<!DOCTYPE html>
<html lang="en">
<head>
<meta charset="utf-8">
<title>Gadget Fix Haven Business Card</title>
<link rel="stylesheet" href="https://fonts.googleapis.com/css2?family=Lato:wght@400;700&family=Comfortaa:wght@500&display=swap">
<style>
  :root {
    --bg: #ececec;
    --card-dark: #000000;
    --card-light: #ffffff;
    --brand-orange: #f0511c;
    --text-gray: #3f3f3f;
    --edge-orange: #e2490f;
  }
  * { margin: 0; padding: 0; box-sizing: border-box; }
  html, body { width: 1200px; height: 1200px; overflow: hidden; }
  body {
    background: var(--bg);
    font-family: "Lato", Arial, sans-serif;
    position: relative;
  }
  .card {
    position: absolute;
    left: 250px;
    width: 700px;
    height: 400px;
    border-bottom: 4px solid var(--edge-orange);
    border-left: 2px solid var(--edge-orange);
    box-shadow: 0 6px 18px rgba(0,0,0,0.12);
  }
  .card-front { top: 110px; background: var(--card-dark); }
  .card-back  { top: 650px; background: var(--card-light); }

  .brand {
    position: absolute;
    left: 110px;
    top: 250px;
    display: flex;
    align-items: center;
    gap: 22px;
  }
  .brand-square {
    width: 64px;
    height: 64px;
    border-radius: 12px;
    background: var(--brand-orange);
  }
  .brand-name {
    font-family: "Comfortaa", "Lato", sans-serif;
    font-weight: 500;
    font-size: 44px;
    color: var(--brand-orange);
    letter-spacing: 0.5px;
  }

  .holder {
    position: absolute;
    left: 90px;
    top: 170px;
  }
  .holder-name {
    font-weight: 700;
    font-size: 30px;
    color: var(--brand-orange);
    text-transform: uppercase;
    letter-spacing: 0.5px;
  }
  .holder-title {
    font-size: 22px;
    color: var(--text-gray);
    margin-top: 4px;
  }
  .divider {
    position: absolute;
    left: 405px;
    top: 90px;
    width: 2px;
    height: 200px;
    background: var(--brand-orange);
  }
  .contact {
    position: absolute;
    left: 435px;
    top: 100px;
    font-size: 21px;
    line-height: 1.3;
    color: var(--text-gray);
  }
  .contact-row { display: flex; gap: 12px; align-items: flex-start; }
  .contact-row + .contact-row { margin-top: 22px; }
  .contact-icon { width: 20px; height: 20px; flex: none; margin-top: 4px; }
</style>
</head>
<body>
  <section class="card card-front" aria-label="Card front">
    <div class="brand">
      <span class="brand-square"></span>
      <span class="brand-name">Gadget Fix Haven</span>
    </div>
  </section>

  <section class="card card-back" aria-label="Card back">
    <div class="holder">
      <p class="holder-name">Wendell Thorsby</p>
      <p class="holder-title">Store Manager</p>
    </div>
    <span class="divider"></span>
    <div class="contact">
      <div class="contact-row">
        <svg class="contact-icon" viewBox="0 0 20 20" aria-hidden="true">
          <rect width="20" height="20" rx="3" fill="var(--brand-orange)"/>
          <path d="M10 4a4 4 0 0 0-4 4c0 3 4 8 4 8s4-5 4-8a4 4 0 0 0-4-4z" fill="#fff"/>
          <circle cx="10" cy="8" r="1.5" fill="var(--brand-orange)"/>
        </svg>
        <address style="font-style:normal">4870 S Ridgecrest Pkwy<br>Suite 318<br>San Antonio, TX 78291</address>
      </div>
      <div class="contact-row">
        <svg class="contact-icon" viewBox="0 0 20 20" aria-hidden="true">
          <rect width="20" height="20" rx="3" fill="var(--brand-orange)"/>
          <path d="M6 4h3l1 3-2 1.2a7 7 0 0 0 3.8 3.8L13 10l3 1v3a2 2 0 0 1-2 2A10 10 0 0 1 4 6a2 2 0 0 1 2-2z" fill="#fff"/>
        </svg>
        <span>(210) 555-0147</span>
      </div>
    </div>
  </section>
</body>
</html>
```